Stationery Design Project

We need, stationary designs for a store of children and juvenile furniture.
we have the logo. also need tags for the furniture with enought space to include description and options , maybe a 4" x 6" tag.

Target Market(s)

Parents of childrens and teens

Industry/Entity Type

Store

```html
<!DOCTYPE html>
<html lang="en">
<head>
<meta charset="utf-8">
<title>Nestling Rooms — Stationery Suite</title>
<link rel="stylesheet" href="https://fonts.googleapis.com/css2?family=Montserrat:wght@400;500;600;700&family=Great+Vibes&display=swap">
<style>
  :root{
    --backdrop:#dadbdb;
    --paper:#f1f2f2;
    --charcoal:#6d6e6f;
    --ink:#5a5b5c;
    --teal:#6fa9b6;
    --rule:#b9bcbd;
    --muted:#8b8d8e;
    --white:#ffffff;
  }
  *{box-sizing:border-box;margin:0;padding:0}
  html,body{width:1200px;height:840px;overflow:hidden}
  body{background:var(--backdrop);font-family:"Montserrat",Arial,sans-serif;color:var(--ink);position:relative}

  .sheet{position:absolute;background:var(--paper);box-shadow:0 6px 16px rgba(0,0,0,.12);overflow:hidden}
  .sheet.dark{background:var(--charcoal)}
  .swoosh{position:absolute;inset:0;width:100%;height:100%}

  .brand{position:absolute;display:flex;align-items:center;gap:7px;font-weight:600;letter-spacing:.08em;text-transform:uppercase;color:var(--ink);white-space:nowrap}
  .brand .mark{display:block;background:var(--teal)}
  .dark .brand{color:var(--white)}

  .fine{position:absolute;font-size:6px;line-height:1.5;color:var(--ink);white-space:nowrap}
  .fine .key{color:var(--teal);font-weight:600}
  .rule{position:absolute;height:1px;background:var(--rule)}

  /* Letterhead */
  .letterhead{left:80px;top:170px;width:340px;height:480px}
  .letterhead .brand{left:50%;top:38px;transform:translateX(-50%);font-size:13px}
  .letterhead .brand .mark{width:14px;height:14px}
  .letterhead .rule.upper{left:70px;right:30px;top:410px}
  .letterhead .fine{left:70px;right:30px;top:420px;text-align:center}
  .letterhead .rule.lower{left:70px;right:30px;top:448px}

  /* Company profile cover */
  .profile{left:450px;top:170px;width:280px;height:396px}
  .profile .brand{left:50%;top:44px;transform:translateX(-50%);font-size:12px}
  .profile .brand .mark{width:13px;height:13px}
  .profile .edge{position:absolute;left:0;top:0;bottom:0;width:5px;background:var(--teal)}
  .profile .title{position:absolute;left:0;right:0;top:220px;text-align:center;color:var(--white);font-weight:600;font-size:22px;line-height:1.15}
  .profile .subtitle{position:absolute;left:0;right:0;top:276px;text-align:center;color:#d7dcdd;font-size:9px;letter-spacing:.2em;text-transform:uppercase}

  /* DL envelope */
  .envelope{left:760px;top:170px;width:360px;height:180px}
  .envelope .brand{left:50%;top:62px;transform:translateX(-50%);font-size:11px}
  .envelope .brand .mark{width:12px;height:12px}
  .envelope .fine{left:0;right:0;top:84px;text-align:center;font-size:5.5px}

  /* Compliment slip */
  .slip{left:760px;top:380px;width:360px;height:180px}
  .slip .brand{left:40px;top:70px;font-size:10px}
  .slip .brand .mark{width:11px;height:11px}
  .slip .greeting{position:absolute;left:176px;top:56px;font-family:"Great Vibes",cursive;font-size:26px;color:var(--teal);white-space:nowrap}
  .slip .rule{left:40px;right:24px;top:116px}
  .slip .fine{left:40px;top:124px;font-size:5.5px}

  /* Business cards */
  .card{width:236px;height:134px;top:622px}
  .card.front{left:450px}
  .card.back{left:710px}
  .card.front .brand{left:50%;top:22px;transform:translateX(-50%);font-size:10px}
  .card.front .brand .mark{width:11px;height:11px}
  .card.front .person{position:absolute;left:0;right:0;top:58px;text-align:center;font-size:8.5px;font-weight:600;letter-spacing:.08em;text-transform:uppercase;color:var(--ink)}
  .card.front .role{position:absolute;left:0;right:0;top:71px;text-align:center;font-size:6px;color:var(--muted)}
  .card.front .fine{left:24px;right:8px;top:90px;text-align:center;font-size:5.5px}
  .card.back .brand{left:50%;top:58px;transform:translateX(-50%);font-size:12px}
  .card.back .brand .mark{width:13px;height:13px}
</style>
</head>
<body>

  <section class="sheet letterhead" aria-label="Letterhead">
    <svg class="swoosh" viewBox="0 0 340 480" preserveAspectRatio="none" aria-hidden="true">
      <path d="M0 210 C 30 290, 46 380, 44 480 L 34 480 C 34 390, 22 300, 0 226 Z" fill="var(--teal)"/>
      <path d="M340 20 C 300 60, 292 100, 340 150 Z" fill="var(--charcoal)"/>
    </svg>
    <div class="brand"><span class="mark"></span>Nestling Rooms</div>
    <div class="rule upper"></div>
    <p class="fine">12 Harbour Lane, Westfield Park NSW 2100 · <span class="key">Tel:</span> +61 2 5550 1842 · <span class="key">Fax:</span> +61 2 5550 1843<br><span class="key">Email:</span> hello@nestlingrooms.com · www.nestlingrooms.com</p>
    <div class="rule lower"></div>
  </section>

  <section class="sheet dark profile" aria-label="Company profile cover">
    <div class="edge"></div>
    <div class="brand"><span class="mark"></span>Nestling Rooms</div>
    <h1 class="title">Leading<br>Innovations</h1>
    <p class="subtitle">Company Profile</p>
  </section>

  <section class="sheet envelope" aria-label="Envelope">
    <svg class="swoosh" viewBox="0 0 360 180" preserveAspectRatio="none" aria-hidden="true">
      <path d="M0 104 C 20 136, 28 160, 30 180 L 22 180 C 20 162, 12 142, 0 118 Z" fill="var(--teal)"/>
      <path d="M290 0 C 320 20, 340 40, 360 70 L 360 0 Z" fill="var(--charcoal)"/>
    </svg>
    <div class="brand"><span class="mark"></span>Nestling Rooms</div>
    <p class="fine">12 Harbour Lane, Westfield Park NSW 2100</p>
  </section>

  <section class="sheet slip" aria-label="Compliment slip">
    <svg class="swoosh" viewBox="0 0 360 180" preserveAspectRatio="none" aria-hidden="true">
      <path d="M0 112 C 20 140, 28 160, 30 180 L 22 180 C 20 162, 12 144, 0 124 Z" fill="var(--teal)"/>
      <path d="M300 0 C 325 15, 345 30, 360 55 L 360 0 Z" fill="var(--charcoal)"/>
    </svg>
    <div class="brand"><span class="mark"></span>Nestling Rooms</div>
    <p class="greeting">With Compliments</p>
    <div class="rule"></div>
    <p class="fine">12 Harbour Lane, Westfield Park NSW 2100 · <span class="key">Tel:</span> +61 2 5550 1842 · <span class="key">Fax:</span> +61 2 5550 1843<br><span class="key">Email:</span> hello@nestlingrooms.com · www.nestlingrooms.com</p>
  </section>

  <section class="sheet card front" aria-label="Business card front">
    <svg class="swoosh" viewBox="0 0 236 134" preserveAspectRatio="none" aria-hidden="true">
      <path d="M0 66 C 12 92, 18 114, 18 134 L 12 134 C 11 116, 7 98, 0 78 Z" fill="var(--teal)"/>
      <path d="M200 0 C 215 12, 228 24, 236 42 L 236 0 Z" fill="var(--charcoal)"/>
    </svg>
    <div class="brand"><span class="mark"></span>Nestling Rooms</div>
    <p class="person">Sam Carter</p>
    <p class="role">Store Manager</p>
    <p class="fine">12 Harbour Lane, Westfield Park NSW 2100<br><span class="key">Tel:</span> +61 2 5550 1842 · <span class="key">Fax:</span> +61 2 5550 1843 · <span class="key">Email:</span> hello@nestlingrooms.com</p>
  </section>

  <section class="sheet dark card back" aria-label="Business card back">
    <div class="brand"><span class="mark"></span>Nestling Rooms</div>
  </section>

</body>
</html>
```